" Venda de joias online. Joias exclusivas. Encomenda de joias. Compra de joias, ou utilização das peças que não servem mais como crédito para peças novas. "

```html
<!DOCTYPE html>
<html lang="pt-BR">
<head>
<meta charset="UTF-8">
<title>Lúmina Joias — Envelope</title>
<link rel="stylesheet" href="https://fonts.googleapis.com/css2?family=Roboto:wght@300;400;500&display=swap">
<style>
  :root {
    --backdrop: #8a8a8a;
    --envelope: #1b1b1c;
    --envelope-edge: #262627;
    --gold: #b39a5c;
    --gold-faint: #4a4333;
    --window: #f4f4f2;
    --ink: #2a2a2a;
    --footer-text: #c9c9c9;
  }
  * { margin: 0; padding: 0; box-sizing: border-box; }
  html, body { width: 1200px; height: 1200px; overflow: hidden; }
  body {
    background: var(--backdrop);
    font-family: "Roboto", Arial, sans-serif;
    position: relative;
  }
  .envelope {
    position: absolute;
    left: 220px; top: 70px;
    width: 760px; height: 1060px;
    background: linear-gradient(160deg, var(--envelope-edge) 0%, var(--envelope) 55%, #141415 100%);
  }
  .address-window {
    position: absolute;
    left: 70px; top: 110px;
    width: 270px; height: 104px;
    background: var(--window);
    border-radius: 4px;
    padding: 18px 22px;
    color: var(--ink);
    font-size: 12px;
    line-height: 17px;
  }
  .brand {
    position: absolute;
    left: 0; right: 0; top: 430px;
    display: flex; align-items: center; justify-content: center; gap: 22px;
  }
  .brand-square {
    width: 38px; height: 38px;
    background: var(--gold-faint);
  }
  .brand-name {
    color: var(--gold-faint);
    font-weight: 300;
    font-size: 72px;
    letter-spacing: 8px;
    text-transform: uppercase;
  }
  .gold-rule {
    position: absolute;
    left: 210px; right: 60px; top: 880px;
    height: 2px;
    background: linear-gradient(90deg, rgba(179,154,92,0) 0%, var(--gold) 40%, var(--gold) 100%);
  }
  .contact {
    position: absolute;
    right: 60px; top: 900px;
    text-align: right;
    color: var(--footer-text);
    font-size: 14px;
    line-height: 22px;
    font-weight: 300;
  }
</style>
</head>
<body>
  <div class="envelope">
    <div class="address-window">
      <p>Ana Ribeiro</p>
      <p>Apto. 783</p>
      <p>Rua das Acácias 215</p>
      <p>Porto Alegre, RS 90010-150</p>
    </div>

    <div class="brand">
      <span class="brand-square"></span>
      <span class="brand-name">Lúmina Joias</span>
    </div>

    <div class="gold-rule"></div>

    <div class="contact">
      <p>+00 (00) 0000 0000 &nbsp; +00 (00) 0000 0000</p>
      <p>www.luminajoias.com.br &nbsp; facebook.com/luminajoias &nbsp; email: contato@luminajoias.com.br</p>
      <p>Endereço | Av. Nome | Nº | Cidade | CEP | UF | Brasil</p>
    </div>
  </div>
</body>
</html>
```